Entrepreneur needs a business card design

I need a business card to name my three companies, as well as contact information.
I'm open on design and color and it can be plain or complex. I'm open on colors but I think I prefer something somewhat formal but fun as well.
I'm open on whether the background is plain or has design in it. I don't have company logos.
Target Market(s)
Auto dealers, realtors and property managers
Industry/Entity Type
Business
Contact Information for Business Card
HALVERSEN FAMILY PROPERTIES, LLC
HALVERSEN PUBLISHING, LLC
MOTORVANE CONSULTING, LLC
Lee Halversen
2871 W. Tamarind Ave. #419
Boise, Idaho 83719-2056
208-514-3092
lee@halv3rn.com

```html
<!DOCTYPE html>
<html lang="en">
<head>
<meta charset="utf-8">
<title>Lee Halversen – Business Card</title>
<link rel="stylesheet" href="https://fonts.googleapis.com/css2?family=Arimo:wght@400;700&display=swap">
<style>
  :root {
    --teal: #0b7d8f;
    --teal-deep: #086676;
    --teal-text: #0f6f80;
    --paper: #ffffff;
    --backdrop: #e9ecee;
  }
  * { box-sizing: border-box; margin: 0; padding: 0; }
  html, body {
    width: 1200px;
    height: 1000px;
    overflow: hidden;
    background: var(--backdrop);
    font-family: "Arimo", Arial, sans-serif;
  }
  .card {
    position: absolute;
    left: 100px;
    top: 214px;
    width: 1000px;
    height: 572px;
    background: var(--paper);
    overflow: hidden;
    box-shadow: 0 10px 30px rgba(0,0,0,0.18);
  }
  .band-top {
    position: absolute;
    left: 560px;
    top: 0;
    width: 440px;
    height: 82px;
    background: var(--teal);
  }
  .panel-contact {
    position: absolute;
    left: 560px;
    top: 196px;
    width: 440px;
    height: 376px;
    background: linear-gradient(160deg, var(--teal) 0%, var(--teal-deep) 100%);
  }
  .identity {
    position: absolute;
    left: 560px;
    width: 440px;
    top: 104px;
    text-align: center;
    color: var(--teal-text);
  }
  .identity .name {
    font-weight: 700;
    font-size: 35px;
    letter-spacing: 0.3px;
  }
  .identity .role {
    font-size: 24px;
    margin-top: 2px;
  }
  .companies {
    position: absolute;
    left: 90px;
    top: 186px;
    list-style: none;
    color: var(--teal-text);
    font-size: 21px;
    letter-spacing: 0.3px;
  }
  .companies li { margin-bottom: 15px; white-space: nowrap; }
  .companies li:nth-child(2) { padding-left: 30px; }
  .companies li:nth-child(3) { padding-left: 10px; }
  .contact {
    position: absolute;
    right: 40px;
    bottom: 56px;
    color: #fff;
    font-size: 23px;
    line-height: 1.4;
    text-align: right;
  }
  .contact .row { display: flex; justify-content: flex-end; align-items: center; gap: 8px; white-space: nowrap; }
  .contact svg { width: 26px; height: 24px; fill: none; stroke: #fff; stroke-width: 1.8; }
</style>
</head>
<body>
  <div class="card">
    <div class="band-top"></div>
    <div class="panel-contact"></div>

    <div class="identity">
      <div class="name">Lee Halversen</div>
      <div class="role">Owner</div>
    </div>

    <ul class="companies">
      <li>HALVERSEN FAMILY PROPERTIES, LLC</li>
      <li>HALVERSEN PUBLISHING, LLC</li>
      <li>MOTORVANE CONSULTING, LLC</li>
    </ul>

    <div class="contact">
      <div class="row">
        <svg viewBox="0 0 26 24" aria-hidden="true"><path d="M3 8c0-3 4-4 10-4s10 1 10 4v2h-5V8H8v2H3z" fill="#fff" stroke="none"/><rect x="6" y="11" width="14" height="10" rx="2" fill="#fff" stroke="none"/></svg>
        <span>: 208-514-3092</span>
      </div>
      <div class="row">
        <svg viewBox="0 0 26 24" aria-hidden="true"><rect x="2" y="5" width="22" height="15"/><path d="M2 5l11 9 11-9"/></svg>
        <span>: lee@halv3rn.com</span>
      </div>
      <div class="row">
        <svg viewBox="0 0 26 24" aria-hidden="true"><path d="M13 16s-6-5-6-9a6 6 0 0112 0c0 4-6 9-6 9z"/><circle cx="13" cy="7" r="2"/><path d="M4 17h5M17 17h5l2 5H2l2-5"/></svg>
        <span>: 2871 W. Tamarind Ave. #419 Boise</span>
      </div>
      <div class="row"><span>Idaho 83719-2056</span></div>
    </div>
  </div>
</body>
</html>
```